Business Card Re-Design

Consulting Company: To build a high performance organization, you need great leaders at all levels throughout your organization. The Cedar Path Talent Institute engages, inspires, and educates current and future leaders to step beyond the ordinary and deliver exceptional results. This new breed of leaders will motivate your staff to leave the safety of complacency behind and come together to build an extraordinary organization. The current trend has been to ask our people to do more with fewer resources. People have been stepping up to the challenge, but more is required to ensure success with a new work paradigm. We work with your management team to build a successful strategy that will make your organization more effective. CPTI then supports your management team by providing a comprehensive set of proven services to empower your entire organization to successfully execute new strategies.Let CPTI help you optimize your organization’s individual and team performance today!

Target Market(s)

Federal, State and Local Government / Non profit

Industry/Entity Type

Management Consulting

Contact Information for Business Card

CPTI, inc (Cedar Path Talent Institute) Optimizing Individual and Organizational Performance

Colors
fee18a
ec1f27
474747
fbf289

Requirements
Must have
• Professional and high quality feel

```html
<!DOCTYPE html>
<html lang="en">
<head>
<meta charset="utf-8">
<title>Cedar Path Talent Institute – Business Card</title>
<link rel="stylesheet" href="https://fonts.googleapis.com/css2?family=Cinzel:wght@400;600&family=EB+Garamond:wght@400&display=swap">
<style>
  :root {
    --red: #ec1f27;
    --charcoal: #474747;
    --gold: #fee18a;
    --pale-yellow: #fbf289;
    --paper: #ffffff;
    --backdrop: #e9e6e1;
    --rule: #b9b9b9;
  }
  * { box-sizing: border-box; margin: 0; padding: 0; }
  html, body {
    width: 1200px; height: 1022px; overflow: hidden;
    background: var(--backdrop);
  }
  .stage {
    width: 1200px; height: 1022px;
    display: flex; align-items: center; justify-content: center;
  }
  .card {
    position: relative;
    width: 1050px; height: 600px;
    background: var(--paper);
    box-shadow: 0 10px 30px rgba(0,0,0,0.12);
    overflow: hidden;
  }
  .edge-stripe { position: absolute; left: 0; top: 70px; width: 22px; }
  .edge-stripe .bar-dark { height: 46px; background: var(--charcoal); }
  .edge-stripe .bar-red { height: 8px; background: var(--red); }
  .top-rule {
    position: absolute; left: 330px; right: 40px; top: 170px;
    height: 1px; background: var(--rule);
  }
  .holder { position: absolute; left: 48px; top: 62px; }
  .holder-name {
    font-family: "Cinzel", serif; font-weight: 600;
    font-size: 40px; letter-spacing: 1px; color: var(--charcoal);
  }
  .holder-title {
    font-family: "Cinzel", serif; font-weight: 400;
    font-size: 24px; color: var(--red); margin-top: 4px;
  }
  .brand-placeholder {
    position: absolute; left: 48px; bottom: 52px;
    display: flex; align-items: center; gap: 14px;
  }
  .brand-placeholder .marker {
    width: 18px; height: 18px; background: var(--charcoal);
  }
  .brand-placeholder .brand-name {
    font-family: "Cinzel", serif; font-weight: 400;
    font-size: 30px; line-height: 1; color: var(--charcoal);
  }
  .contact {
    position: absolute; right: 56px; bottom: 130px;
    list-style: none; text-align: right;
    font-family: "EB Garamond", serif; font-size: 28px;
    color: var(--charcoal); line-height: 1.4;
  }
  .contact li { display: flex; align-items: center; justify-content: flex-end; gap: 12px; }
  .contact svg { width: 20px; height: 20px; flex: none; }
  .company-name {
    position: absolute; right: 56px; bottom: 44px;
    font-family: "Cinzel", serif; font-weight: 400;
    font-size: 46px; letter-spacing: 1px; color: var(--red);
    text-align: right; white-space: nowrap;
  }
</style>
</head>
<body>
<main class="stage">
  <article class="card">
    <div class="edge-stripe"><div class="bar-dark"></div><div class="bar-red"></div></div>
    <div class="top-rule"></div>

    <header class="holder">
      <h1 class="holder-name">DANIEL R. WHITFORD</h1>
      <p class="holder-title">PRESIDENT/CEO</p>
    </header>

    <div class="brand-placeholder">
      <span class="marker"></span>
      <span class="brand-name">CPTI, inc</span>
    </div>

    <ul class="contact">
      <li>410-555-0142
        <svg viewBox="0 0 20 20" aria-hidden="true"><path d="M5 2 L8 6 L6 8 Q8 12 12 14 L14 12 L18 15 L16 18 Q8 18 2 6 Z" fill="none" stroke="#ec1f27" stroke-width="1.6"/></svg>
      </li>
      <li>dwhitford@cptiinc.com
        <svg viewBox="0 0 20 20" aria-hidden="true"><rect x="2" y="4" width="16" height="12" fill="none" stroke="#ec1f27" stroke-width="1.6"/><path d="M2 4 L10 11 L18 4" fill="none" stroke="#ec1f27" stroke-width="1.6"/></svg>
      </li>
      <li>www.cptiinc.com
        <svg viewBox="0 0 20 20" aria-hidden="true"><circle cx="10" cy="10" r="8" fill="none" stroke="#ec1f27" stroke-width="1.6"/><ellipse cx="10" cy="10" rx="3.5" ry="8" fill="none" stroke="#ec1f27" stroke-width="1.2"/><path d="M2 10 H18 M3.5 6 H16.5 M3.5 14 H16.5" stroke="#ec1f27" stroke-width="1.2"/></svg>
      </li>
    </ul>

    <p class="company-name">Cedar Path Talent Institute</p>
  </article>
</main>
</body>
</html>
```